Tavrelo.com.au - AV and Communications Installation Company Website

A company website for a modern, high level/enterprise communications installation/engineering company based in Sydney Australia.
My client base is construction companies working in medical, government and educations departments so the website needs to look professional.
Clients like Quenby or Dorvik as I want to eventually move into data centre design and installation so I need something appealing to the high end market.
Fiber Optic Installation is a massive part of the company aswell.
Audio visual, IT installation is also what the company will be involved in.
I want the website to be modern, eye catching, professional looking.

Target Market(s)

High end clients and construction companies

Industry/Entity Type

Communications

Coding

Coded - Design and coding required

Number of Pages Required

1 page

Requirements
Must have
• Modern and clean layout with links to other social media platforms

```html
<!DOCTYPE html>
<html lang="en">
<head>
<meta charset="utf-8">
<title>Tavrelo – AV &amp; Communication Installation</title>
<link rel="stylesheet" href="https://fonts.googleapis.com/css2?family=Poppins:wght@300;400;500;600;700&family=Bebas+Neue&display=swap">
<style>
:root{
  --teal:#1b96a1;
  --teal-soft:#e3f2f3;
  --ink:#1d1d1d;
  --muted:#6f6f6f;
  --light:#f4f4f4;
  --white:#ffffff;
  --black:#000000;
}
*{box-sizing:border-box;margin:0;padding:0}
html,body{width:1200px;height:4156px;overflow:hidden}
body{font-family:'Poppins',sans-serif;color:var(--ink);background:var(--white);position:relative}
.abs{position:absolute}
a{color:inherit;text-decoration:none}

/* hero */
.hero{left:0;top:0;width:1200px;height:676px;background:radial-gradient(ellipse at 70% 30%,#8a7a2e 0%,#3b3f3a 35%,#1d2a36 70%,#121a22 100%)}
.hero-shade{left:0;top:0;width:1200px;height:676px;background:linear-gradient(90deg,rgba(10,14,20,.75) 0%,rgba(10,14,20,.35) 55%,rgba(10,14,20,.1) 100%)}
.brand{display:flex;align-items:center;gap:10px;font-family:'Poppins',sans-serif;font-weight:500;color:var(--teal);letter-spacing:1px}
.brand-dot{width:18px;height:18px;border-radius:50%;background:var(--teal)}
.nav{top:40px;left:622px;display:flex;gap:29px;font-size:14px;color:var(--white);border-left:3px solid var(--teal);padding-left:10px;height:34px;align-items:center}
.nav .active{color:var(--teal)}
.hero-title{left:79px;top:258px;font-size:37px;font-weight:700;color:var(--white);line-height:47px;letter-spacing:.5px}
.hero-name{left:79px;top:356px;font-family:'Bebas Neue',sans-serif;font-size:72px;color:var(--teal);letter-spacing:1px;line-height:1}
.btn-solid{left:77px;top:444px;width:188px;height:56px;background:var(--teal);color:var(--white);font-size:20px;display:flex;align-items:center;justify-content:center;border-radius:3px}
.slide-arrow{top:346px;width:52px;height:52px;border-radius:50%;background:rgba(0,0,0,.35);display:flex;align-items:center;justify-content:center}
.quote{left:879px;top:637px;width:321px;height:82px;background:var(--teal);color:var(--white);font-size:22px;display:flex;align-items:center;justify-content:center;gap:18px}

/* section heads */
.eyebrow{font-size:18px;color:var(--teal);display:flex;align-items:center;gap:12px}
.eyebrow::before{content:"";width:57px;height:1px;background:var(--teal);display:block}
.heading{font-size:44px;font-weight:600;color:var(--ink)}

/* services */
.service{width:270px}
.service-icon{width:100px;height:110px;position:relative}
.service-icon .blob{position:absolute;left:30px;top:30px;width:56px;height:56px;border-radius:50%;background:var(--teal-soft)}
.service-icon svg{position:absolute;left:0;top:0}
.service h3{font-size:20px;font-weight:500;margin-top:30px}
.service p{font-size:14px;line-height:27px;color:var(--muted);margin-top:16px}
.more{font-size:14px;color:var(--teal);margin-top:14px;display:flex;align-items:center;gap:6px}
.tri{width:0;height:0;border-top:5px solid transparent;border-bottom:5px solid transparent;border-left:7px solid currentColor;display:inline-block}

/* welcome */
.welcome-band{left:0;top:1255px;width:948px;height:551px;background:var(--teal)}
.welcome-photo{left:637px;top:1327px;width:563px;height:541px;background:linear-gradient(135deg,#1b1b1e 0%,#2b3a48 30%,#3d8fb8 45%,#c85a22 65%,#e07a32 80%,#2a2320 100%)}
.welcome-text{left:165px;top:1423px;width:412px;font-size:16px;line-height:27px;color:var(--white)}
.btn-line{border:2px solid var(--white);color:var(--white);font-size:19px;display:flex;align-items:center;justify-content:center;border-radius:4px}

/* industry */
.card{top:2073px;width:282px}
.card-img{width:282px;height:253px}
.card h4{font-size:20px;font-weight:500;margin-top:32px}
.card .sub{font-size:14px;color:var(--muted);margin-top:4px}
.card .play{position:absolute;right:8px;top:291px;width:36px;height:36px;border-radius:50%;background:var(--teal);display:flex;align-items:center;justify-content:center;color:var(--white)}
.card .rule{position:absolute;left:0;top:357px;width:282px;height:3px;background:var(--teal)}

/* news */
.news{left:0;top:2510px;width:1200px;height:624px;background:var(--light)}
.news-photo{left:210px;top:2703px;width:427px;height:352px;background:linear-gradient(160deg,#6f7a78 0%,#3e4a4a 40%,#c06a2a 55%,#2b2f33 100%)}

/* contact */
.contact-band{left:0;top:3134px;width:729px;height:624px;background:var(--teal)}
.black-strip{left:729px;top:3640px;width:471px;height:118px;background:var(--black)}
.field{left:166px;width:444px;border-bottom:1px solid rgba(255,255,255,.7);color:var(--white);font-size:15px;padding-bottom:12px}
.info{left:780px;display:flex;gap:22px;align-items:flex-start}
.info-ico{width:58px;height:58px;border-radius:50%;border:2px solid var(--teal);display:flex;align-items:center;justify-content:center;flex:none}
.info p{font-size:14px;line-height:27px;color:var(--muted)}

/* footer */
.foot-head{font-size:21px;font-weight:500;color:#8a8a8a}
.foot-list{list-style:none;font-size:15px;line-height:27px;color:var(--ink)}
.foot-list li{display:flex;align-items:center;gap:16px}
.foot-list li::before{content:"";width:6px;height:6px;border-radius:50%;background:var(--teal)}
.social{width:52px;height:52px;border-radius:50%;background:var(--teal)}
</style>
</head>
<body>

<!-- hero -->
<div class="abs hero" role="img" aria-label="Close-up of network switches with yellow fibre optic patch cables"></div>
<div class="abs hero-shade"></div>
<div class="abs brand" style="left:77px;top:30px;font-size:44px"><span class="brand-dot"></span>Tavrelo</div>
<nav class="abs nav">
  <a class="active">HOME</a><a>ABOUT</a><a>SERVICES</a><a>INDUSTRIES</a><a>NEWS</a><a>CONTACT</a>
</nav>
<h1 class="abs hero-title">AV &amp; COMMUNICATION<br>INSTALLATION</h1>
<div class="abs hero-name">TAVRELO COMPANY</div>
<a class="abs btn-solid">CONTACT US</a>
<div class="abs slide-arrow" style="left:11px"><svg width="14" height="22" viewBox="0 0 14 22"><path d="M11 2 2 11l9 9" fill="none" stroke="#bbb" stroke-width="2"/></svg></div>
<div class="abs slide-arrow" style="left:1137px"><svg width="14" height="22" viewBox="0 0 14 22"><path d="M3 2l9 9-9 9" fill="none" stroke="#bbb" stroke-width="2"/></svg></div>
<a class="abs quote">REQUEST A QUOTE <span class="tri" style="border-top-width:8px;border-bottom-width:8px;border-left-width:11px"></span></a>

<!-- services -->
<div class="abs eyebrow" style="left:97px;top:763px">What We Do</div>
<h2 class="abs heading" style="left:159px;top:788px">Our Services</h2>

<div class="abs service" style="left:163px;top:885px">
  <div class="service-icon"><span class="blob"></span>
    <svg width="100" height="110" viewBox="0 0 100 110" fill="none" stroke="#1b96a1" stroke-width="2"><path d="M8 6v24M14 2v28M20 6v24M26 2v28M32 6v24M38 2v28"/><rect x="6" y="30" width="36" height="14"/><path d="M10 44v10h28V44M10 54v46M38 54v46M10 70h28"/></svg>
  </div>
  <h3>Fiber Optic Installation</h3>
  <p>Lorem Ipsum is simply dummy text of the printing and type setting the industry Lorem Ipsum</p>
  <a class="more">Learn More <span class="tri"></span></a>
</div>
<div class="abs service" style="left:468px;top:885px">
  <div class="service-icon"><span class="blob"></span>
    <svg width="100" height="110" viewBox="0 0 100 110" fill="none" stroke="#1b96a1" stroke-width="2"><path d="M12 40a28 28 0 0 1 56 0"/><rect x="4" y="38" width="12" height="24" rx="5"/><rect x="64" y="38" width="12" height="24" rx="5"/><path d="M70 62c0 14-10 20-26 20"/><circle cx="40" cy="82" r="4"/><path d="M30 50h2M38 50h2M46 50h2"/></svg>
  </div>
  <h3>Audio Visual</h3>
  <p>Lorem Ipsum is simply dummy text of the printing and type setting the industry Lorem Ipsum</p>
  <a class="more">Learn More <span class="tri"></span></a>
</div>
<div class="abs service" style="left:771px;top:885px">
  <div class="service-icon"><span class="blob"></span>
    <svg width="100" height="110" viewBox="0 0 100 110" fill="none" stroke="#1b96a1" stroke-width="2"><rect x="3" y="6" width="52" height="76" rx="4"/><circle cx="29" cy="38" r="16"/><circle cx="29" cy="38" r="5"/><path d="M24 46 14 66"/><circle cx="9" cy="12" r="1.5"/><circle cx="49" cy="12" r="1.5"/><circle cx="9" cy="76" r="1.5"/><circle cx="49" cy="76" r="1.5"/></svg>
  </div>
  <h3>IT Installation</h3>
  <p>Lorem Ipsum is simply dummy text of the printing and type setting the industry Lorem Ipsum</p>
  <a class="more">Learn More <span class="tri"></span></a>
</div>

<!-- welcome -->
<div class="abs welcome-band"></div>
<div class="abs welcome-photo" role="img" aria-label="Fibre patch panel with blue connectors and orange optic cables in a rack"></div>
<div class="abs eyebrow" style="left:99px;top:1310px;color:var(--white)"><span style="display:none"></span>Welcome To</div>
<style>.welcome-eyebrow::before{background:#fff}</style>
<h2 class="abs heading" style="left:162px;top:1340px;color:var(--white)">Tavrelo</h2>
<p class="abs welcome-text">Lorem Ipsum is simply dummy text of the printing and typesetting industry. Lorem Ipsum has been the industry's standard dummy text ever since the 1500s, when an unknown printer took a galley of type and scrambled it to make a type specimen book. It has survived not only five centuries, but also the leap into electronic typesetting, remaining essentially unchanged.</p>
<a class="abs btn-line" style="left:163px;top:1663px;width:187px;height:61px">LEARN MORE</a>

<!-- industry -->
<div class="abs eyebrow" style="left:97px;top:1938px">Working On</div>
<h2 class="abs heading" style="left:161px;top:1964px">Our Industry</h2>
<p class="abs" style="left:582px;top:1961px;width:460px;font-size:14px;line-height:27px;color:var(--muted)">Lorem Ipsum is simply dummy text of the printing and type setting the industry Lorem Ipsum</p>

<div class="abs card" style="left:160px">
  <div class="card-img" role="img" aria-label="Medical endoscope tip on blue surgical cloth" style="background:linear-gradient(135deg,#3aa6d6,#1f6f9e)"></div>
  <h4>Medical</h4><p class="sub">Lorem Ipsum is simply text.</p>
  <span class="play"><span class="tri"></span></span><span class="rule"></span>
</div>
<div class="abs card" style="left:460px">
  <div class="card-img" role="img" aria-label="Technician climbing down into a cable pit" style="background:radial-gradient(circle at 50% 45%,#3a3a34 0%,#6b5a44 55%,#9a9384 100%)"></div>
  <h4>Government</h4><p class="sub">Lorem Ipsum is simply text.</p>
  <span class="play"><span class="tri"></span></span><span class="rule"></span>
</div>
<div class="abs card" style="left:758px">
  <div class="card-img" role="img" aria-label="Technician testing cables at a workbench" style="background:linear-gradient(135deg,#d8d4cc,#8a8176 55%,#2a3244)"></div>
  <h4>Educations</h4><p class="sub">Lorem Ipsum is simply text.</p>
  <span class="play"><span class="tri"></span></span><span class="rule"></span>
</div>

<!-- news -->
<div class="abs news"></div>
<div class="abs eyebrow" style="left:97px;top:2580px">Tavrelo</div>
<h2 class="abs heading" style="left:161px;top:2606px">Latest News</h2>
<svg class="abs" style="left:1046px;top:2596px" width="54" height="30" viewBox="0 0 54 30" fill="none" stroke="#1b96a1" stroke-width="2"><path d="M14 2 2 15l12 13M40 2l12 13-12 13"/></svg>
<div class="abs news-photo" role="img" aria-label="Field technicians in hard hats laying fibre cable outdoors"></div>
<p class="abs" style="left:682px;top:2746px;font-size:15px;font-weight:600;color:var(--teal)">28 April 2020</p>
<h3 class="abs" style="left:682px;top:2774px;width:330px;font-size:21px;font-weight:500;line-height:31px">Lorem Ipsum is simply Dummy Text of the Printing Type.</h3>
<p class="abs" style="left:684px;top:2851px;width:320px;font-size:14px;line-height:27px;color:var(--muted)">Lorem Ipsum is simply dummy text of the printing and typesetting industry. Lorem Ipsum has been the industry's standard dummy text ever since the.</p>
<a class="abs more" style="left:687px;top:2974px;font-size:19px">Learn More <span class="tri"></span></a>

<!-- contact -->
<div class="abs contact-band"></div>
<div class="abs black-strip"></div>
<div class="abs eyebrow" style="left:97px;top:3201px;color:var(--white)">Keep n Touch</div>
<h2 class="abs heading" style="left:161px;top:3228px;color:var(--white)">Contact Us</h2>
<div class="abs field" style="top:3319px">Name *</div>
<div class="abs field" style="top:3393px">Email *</div>
<div class="abs field" style="top:3467px">Phone *</div>
<div class="abs field" style="top:3542px;height:74px">Message *</div>
<a class="abs btn-line" style="left:165px;top:3640px;width:229px;height:63px">SEND A MESSAGE</a>

<h3 class="abs" style="left:784px;top:3222px;font-size:27px;font-weight:600">Get In Touch</h3>
<div class="abs info" style="top:3290px">
  <span class="info-ico"><svg width="28" height="28" viewBox="0 0 28 28" fill="none" stroke="#1b96a1" stroke-width="1.6"><path d="M14 3a6 6 0 0 1 6 6c0 5-6 10-6 10S8 14 8 9a6 6 0 0 1 6-6z"/><circle cx="14" cy="9" r="2"/><path d="M4 20l5-2 10 3 5-2v6l-5 2-10-3-5 2z"/></svg></span>
  <p>Tavrelo<br>101 – Lorem ipsum simple<br>text print industry.</p>
</div>
<div class="abs info" style="top:3385px">
  <span class="info-ico"><svg width="26" height="26" viewBox="0 0 26 26" fill="none" stroke="#1b96a1" stroke-width="1.6"><path d="M6 3l4 5-2 3c1 3 4 6 7 7l3-2 5 4-3 4C11 24 2 15 2 6z"/></svg></span>
  <p>Phone :<br>02 5550 1847</p>
</div>
<div class="abs info" style="top:3468px">
  <span class="info-ico"><svg width="26" height="20" viewBox="0 0 26 20" fill="none" stroke="#1b96a1" stroke-width="1.6"><rect x="2" y="2" width="22" height="16" rx="2"/><path d="M2 4l11 8 11-8"/></svg></span>
  <p>Email :<br>info@tavrelo.com.au</p>
</div>

<!-- footer -->
<div class="abs brand" style="left:77px;top:3806px;font-size:48px"><span class="brand-dot"></span>Tavrelo</div>
<p class="abs" style="left:79px;top:3883px;width:250px;font-size:14px;line-height:25px">Lorem Ipsum is simply dummy text of the printing &amp; type setting industry. Lorem Ipsum has been the industry's standard dummy text ever since the.</p>
<a class="abs more" style="left:79px;top:4017px;font-size:15px;margin:0">Learn More <span class="tri"></span></a>

<h4 class="abs foot-head" style="left:381px;top:3832px">Quick Links</h4>
<ul class="abs foot-list" style="left:381px;top:3883px">
  <li>Home</li><li>About</li><li>Services</li><li>Industries</li><li>News</li><li>Contact</li>
</ul>
<h4 class="abs foot-head" style="left:623px;top:3832px">Services</h4>
<ul class="abs foot-list" style="left:623px;top:3883px">
  <li>Fiber Optic Installation</li><li>Audio visual</li><li>IT installation</li>
</ul>
<h4 class="abs foot-head" style="left:866px;top:3832px">Follow Us</h4>
<a class="abs social" style="left:869px;top:3892px" aria-label="Social profile one"></a>
<a class="abs social" style="left:927px;top:3892px" aria-label="Social profile two"></a>
<a class="abs social" style="left:986px;top:3892px" aria-label="Social profile three"></a>

<div class="abs" style="left:79px;top:4082px;width:1042px;height:1px;background:#e2e2e2"></div>
<p class="abs" style="left:0;top:4108px;width:1200px;text-align:center;font-size:14px">©<span style="color:var(--teal)">Tavrelo</span>– 2020 All rights reserved</p>

</body>
</html>
```